We need UI/UX design for a public, informational website for The Harbor Lens.
The pages, structure, and content scope are already defined. Designers are required to work only on the UI/UX layout of these existing pages, focusing on clarity, hierarchy, spacing, and usability. Do not add, remove, rename, or reinterpret pages or content.
The website is strictly informational only. It must not include accounts, onboarding, payments, custody, escrow administration, marketplaces, dashboards, or any transactional functionality.
Scope of work
Apply UI/UX design to the predefined website pages
Design layout for text, images, notices, and sections
Ensure consistent components and layout patterns across page types
Optimize layouts for long form, compliance focused content
Content writing, page creation, and branding changes are out of scope.
Structure reference
The complete page list, hierarchy, and content definitions are provided in the technical documentation and must be treated as the primary source of truth.
A Figma link is provided only as a light visual reference for page existence and structure:
https://kettle-marsh-48203956.example-site.net/
Designers must rely on the documentation for in depth and authoritative reference.
Brand guidelines
The Harbor Lens has existing brand guidelines and official logos, including light and dark versions. These assets will be provided and must be followed exactly. Designers must not redesign, alter, or reinterpret the brand identity.
Look and feel direction
The desired visual direction is inspired by:
https://vantorum.example/
This reference is provided only to indicate:
Institutional and enterprise tone
Clean, modern typography
Strong hierarchy and generous whitespace
Editorial, content first layouts
Do not copy branding, layouts, components, or assets from the reference site.
Hero section direction
The hero section should follow a similar structural approach to the hero used on https://vantorum.example/
, meaning:
Strong editorial framing
Clear headline hierarchy
Calm, institutional first impression
However, the background video must be Abu Dhabi focused, not generic or global. The video should visually reflect:
Abu Dhabi skyline or architectural language
Institutional, sovereign, long term infrastructure tone
Clean, slow, cinematic motion
No promotional, marketing, or lifestyle visuals
The hero must remain informational, restrained, and credible. No hype. No calls to invest. No implied participation.
Constraints
One global primary CTA only: “Continue to Brightvault” (external)
All other interactions must be informational
No visuals or language implying offers, investment, eligibility, or participation
Clear separation between informational content and any external operational platforms
Deliverables
High fidelity UI/UX designs created in Figma, covering:
Desktop layouts
Tablet layouts where relevant
Mobile layouts
Complete Figma file(s) including:
All designed pages defined in the technical documentation
A reusable component library (headers, footers, cards, notice panels, forms, CTAs, typography styles, spacing system)
Clearly defined layout grids, spacing rules, and text styles
Proper use of components and variants, not detached frames
Designs prepared for developer handoff, including:
Clear layer naming and structure
Auto layout where appropriate
Consistent use of styles and components
Responsive behavior demonstrated within Figma
Notes or annotations only where necessary for clarity
No prototypes, interactions, or motion design beyond basic layout states, unless explicitly requested. The focus is static UI/UX clarity, not animation.
A detailed technical specification document and official brand assets will be provided.
Any designs delivered outside Figma, that alter structure or content, or that ignore the defined constraints, boundaries, or tone will be rejected.

```html
<!DOCTYPE html>
<html lang="en">
<head>
<meta charset="utf-8">
<title>The Harbor Lens — Governance Framework</title>
<link href="https://fonts.googleapis.com/css2?family=Space+Grotesk:wght@500;600;700&family=Inter:wght@400;500;600&display=swap" rel="stylesheet">
<style>
:root{
  --canvas:#b9b9b9;
  --page:#0b0b0b;
  --band:#151515;
  --card:#1c1c1c;
  --line:#2e2e2e;
  --text:#f2f2f2;
  --muted:#9a9a9a;
  --dim:#6d6d6d;
  --white:#ffffff;
}
*{box-sizing:border-box;margin:0;padding:0}
html,body{width:1200px;height:3248px;overflow:hidden}
body{background:var(--canvas);font-family:"Inter",sans-serif;color:var(--text)}
.page{position:absolute;left:80px;top:0;width:1040px;height:3200px;background:var(--page);overflow:hidden}
h1,h2,h3,.display{font-family:"Space Grotesk",sans-serif;font-weight:600;letter-spacing:-.01em}
.container{width:820px;margin:0 auto;position:relative}
.eyebrow{font-size:9px;color:var(--muted);letter-spacing:.04em}
.btn{display:inline-block;background:var(--white);color:#111;font-size:10px;font-weight:600;padding:7px 14px;border-radius:999px}
p{font-size:9px;line-height:1.55;color:var(--muted)}

/* hero */
.hero{position:relative;height:810px}
.hero-media{position:absolute;inset:0;background:radial-gradient(ellipse at 50% 60%,#3d3d3d 0%,#252525 45%,#0f0f0f 100%)}
.hero-shade{position:absolute;inset:0;background:linear-gradient(180deg,rgba(0,0,0,.35) 0%,rgba(0,0,0,.15) 50%,rgba(0,0,0,.8) 100%)}
.nav{position:absolute;left:24px;right:24px;top:18px;display:flex;align-items:center;justify-content:space-between}
.brand{display:flex;align-items:center;gap:8px;font-family:"Inter",sans-serif;font-size:11px;font-weight:600;color:var(--text)}
.brand-dot{width:22px;height:22px;border:1.5px solid var(--text);border-radius:50%}
.nav-links{display:flex;gap:20px;font-size:10px;color:#cfcfcf}
.nav-links .active{color:var(--white);font-weight:600}
.nav .btn{font-size:9px;padding:6px 12px}
.hero-copy{position:absolute;left:0;right:0;top:400px;text-align:center}
.hero-copy h1{font-size:44px;line-height:1.12;color:var(--white)}
.hero-copy p{font-size:14px;color:#dcdcdc;margin:18px auto 26px;width:460px;line-height:1.45}

/* about */
.about{height:390px;padding-top:56px;border-bottom:1px solid var(--line)}
.about .container{display:flex;gap:40px}
.about-text{width:400px}
.about-text h2{font-size:27px;line-height:1.15;margin:8px 0 14px}
.about-text p{margin-bottom:18px}
.about-media{display:flex;gap:14px}
.tile{width:176px}
.tile .ph{height:160px;background:linear-gradient(160deg,#5a5a5a,#2a2a2a)}
.tile span{display:block;text-align:center;font-size:9px;color:#cfcfcf;margin-top:8px}

/* role */
.role{height:435px;padding-top:36px;background:var(--band)}
.center{text-align:center}
.role h2{font-size:26px;margin:6px 0 22px}
.role-grid{display:grid;grid-template-columns:repeat(3,1fr);gap:14px}
.role-card{background:var(--card);border:1px solid var(--line)}
.role-card .ph{height:140px;background:linear-gradient(170deg,#6a6a6a,#2c2c2c)}
.role-card .body{padding:12px 14px 14px}
.role-card h3{font-size:14px;margin-bottom:6px}
.role-card p{margin-bottom:10px}
.row{display:flex;justify-content:space-between;font-size:8px;padding:5px 0;border-top:1px solid var(--line);color:var(--muted)}
.row b{color:var(--text);font-weight:500}

/* framework */
.framework{height:395px;padding-top:50px;border-bottom:1px solid var(--line)}
.framework .container{display:flex;justify-content:space-between}
.fw-intro{width:300px;padding-top:22px}
.fw-intro h2{font-size:28px;margin:8px 0 10px}
.fw-list{width:420px}
.fw-num{font-size:9px;color:var(--muted)}
.fw-open h3{font-size:18px;margin:4px 0 6px}
.fw-open p{margin-bottom:14px}
.fw-item{display:flex;justify-content:space-between;align-items:center;font-family:"Space Grotesk",sans-serif;font-size:13px;font-weight:500;padding:9px 0;border-bottom:1px solid var(--line)}
.fw-item:first-of-type{border-top:1px solid var(--line)}

/* reviewers */
.reviewers{height:330px;padding-top:40px;background:var(--band)}
.reviewers h2{font-size:24px;margin-bottom:26px}
.rv-grid{display:grid;grid-template-columns:repeat(4,1fr);gap:12px}
.rv-card{border:1px solid #3a3a3a;padding:14px;height:150px}
.rv-card h3{font-size:12px;line-height:1.25;margin-bottom:8px}

/* why */
.why{height:390px;padding-top:44px}
.why h2{font-size:26px;margin-bottom:34px}
.why-grid{display:grid;grid-template-columns:1fr 1fr;row-gap:30px;column-gap:60px;width:720px;margin:0 auto;text-align:center}
.why-grid h3{font-size:13px;margin-bottom:6px}

/* cta */
.cta{height:290px;padding-top:60px;background:var(--band);text-align:center}
.cta h2{font-size:28px;line-height:1.12;margin:8px 0 12px;text-transform:uppercase}
.cta p{width:420px;margin:0 auto 18px}

/* footer */
.footer{height:160px;padding-top:30px;border-top:1px solid var(--line)}
.ft-cols{display:grid;grid-template-columns:1.6fr 1fr 1fr 1fr;gap:30px}
.ft-cols h4{font-size:9px;font-weight:600;margin-bottom:8px}
.ft-cols li{list-style:none;font-size:8px;color:var(--muted);margin-bottom:4px}
.ft-base{margin-top:16px;padding-top:10px;border-top:1px solid var(--line);font-size:7.5px;color:var(--dim);display:flex;justify-content:space-between}
</style>
</head>
<body>
<div class="page">

  <section class="hero">
    <div class="hero-media" role="img" aria-label="Aerial view of the Abu Dhabi skyline at dusk, in muted greyscale"></div>
    <div class="hero-shade"></div>
    <nav class="nav">
      <div class="brand"><span class="brand-dot"></span>The Harbor Lens</div>
      <div class="nav-links"><span class="active">Home</span><span>Framework</span><span>Projects</span><span>Governance</span><span>Insights</span><span>Contact</span></div>
      <span class="btn">Continue to Brightvault</span>
    </nav>
    <div class="hero-copy">
      <h1>A Governance Framework for<br>Structured Project Oversight</h1>
      <p>Clear boundaries. Institutional discipline. Transparent structures for managing risk and accountability.</p>
      <span class="btn">Learn Our Framework</span>
    </div>
  </section>

  <section class="about">
    <div class="container">
      <div class="about-text">
        <div class="eyebrow">About The Harbor Lens</div>
        <h2>From Governance Frameworks to Intelligent Infrastructure</h2>
        <p>The Harbor Lens sets out a governance reference for structured projects, defining roles, boundaries and oversight. Our purpose is to document how long-term infrastructure is organised, recorded and reviewed, so that every participant understands where responsibility sits.</p>
        <span class="btn">Our Framework</span>
      </div>
      <div class="about-media">
        <div class="tile"><div class="ph" role="img" aria-label="Modern tower architecture in greyscale"></div><span>Independent Oversight Principles</span></div>
        <div class="tile"><div class="ph" role="img" aria-label="Water tower structure against a pale sky"></div><span>Institutional Grade Standards</span></div>
      </div>
    </div>
  </section>

  <section class="role">
    <div class="container">
      <div class="center"><div class="eyebrow">Our Scope</div><h2>Understanding Our Role</h2></div>
      <div class="role-grid">
        <div class="role-card">
          <div class="ph" role="img" aria-label="Government building facade in greyscale"></div>
          <div class="body"><h3>Governance</h3><p>We define the oversight structures that keep each project accountable and documented.</p>
            <div class="row"><span>Oversight</span><b>Structured Framework</b></div>
            <div class="row"><span>Standards</span><b>Institutional &amp; Public Reference</b></div>
            <div class="row"><span>Reference</span><b>International Use Only</b></div></div>
        </div>
        <div class="role-card">
          <div class="ph" role="img" aria-label="Curved concrete building in greyscale"></div>
          <div class="body"><h3>Operations</h3><p>We describe how operational duties are separated from governance and external platforms.</p>
            <div class="row"><span>Oversight</span><b>Structured Framework</b></div>
            <div class="row"><span>Standards</span><b>Institutional &amp; Public Reference</b></div>
            <div class="row"><span>Reference</span><b>International Use Only</b></div></div>
        </div>
        <div class="role-card">
          <div class="ph" role="img" aria-label="City skyline with high-rise towers in greyscale"></div>
          <div class="body"><h3>Transactions</h3><p>We explain where records are held and which boundaries apply to each transaction.</p>
            <div class="row"><span>Oversight</span><b>Structured Framework</b></div>
            <div class="row"><span>Standards</span><b>Institutional &amp; Public Reference</b></div>
            <div class="row"><span>Reference</span><b>International Use Only</b></div></div>
        </div>
      </div>
    </div>
  </section>

  <section class="framework">
    <div class="container">
      <div class="fw-intro">
        <div class="eyebrow">Core Governance Principles</div>
        <h2>The Framework</h2>
        <p>A structured set of principles defining oversight, accountability and clear boundaries.</p>
      </div>
      <div class="fw-list">
        <div class="fw-open">
          <div class="fw-num">01</div>
          <h3>Role Boundaries</h3>
          <p>Each participant holds a defined role with documented responsibilities, keeping oversight separate from operational execution and external platforms.</p>
        </div>
        <div class="fw-item">SPV Structure<span>+</span></div>
        <div class="fw-item">Escrow Model<span>+</span></div>
        <div class="fw-item">Records and Registers<span>+</span></div>
        <div class="fw-item">Risk and Boundaries<span>+</span></div>
      </div>
    </div>
  </section>

  <section class="reviewers">
    <div class="container">
      <h2 class="center">For Framework Reviewers</h2>
      <div class="rv-grid">
        <div class="rv-card"><h3>Review Governance Structures</h3><p>Assess how oversight layers are defined, documented and maintained over time.</p></div>
        <div class="rv-card"><h3>Defined Structural Ownership</h3><p>Each structure has a clear owner with recorded duties and review points.</p></div>
        <div class="rv-card"><h3>Operational Independence</h3><p>Governance remains separate from operations and any external platform.</p></div>
        <div class="rv-card"><h3>Clear Access Boundaries</h3><p>The site is informational only, with no accounts or transactional features.</p></div>
      </div>
    </div>
  </section>

  <section class="why">
    <div class="container">
      <h2 class="center">Why The Harbor Lens</h2>
      <div class="why-grid">
        <div><h3>Governance-First Approach</h3><p>Structures are designed around oversight before execution, keeping accountability visible.</p></div>
        <div><h3>Proven Structural Principles</h3><p>The framework draws on established institutional practice and public reference standards.</p></div>
        <div><h3>Bridging Structure &amp; Execution</h3><p>Clear documentation links governance decisions to how projects are carried out.</p></div>
        <div><h3>Defined Control &amp; Boundaries</h3><p>Every control point is recorded, with boundaries that remain consistent over time.</p></div>
      </div>
    </div>
  </section>

  <section class="cta">
    <div class="eyebrow">FOR PROJECT ORIGINATORS</div>
    <h2>Define Your Project's<br>Governance Framework</h2>
    <p>Review how structures define responsibility, boundaries and oversight for projects before any external discussion.</p>
    <span class="btn">Start a Framework Discussion</span>
  </section>

  <footer class="footer">
    <div class="container">
      <div class="ft-cols">
        <div><h4>The Harbor Lens</h4><p>An informational governance reference for structured project oversight.</p></div>
        <div><h4>Framework</h4><ul><li>Role Boundaries</li><li>SPV Structure</li><li>Escrow Model</li><li>Records</li></ul></div>
        <div><h4>Company</h4><ul><li>About</li><li>Governance</li><li>Insights</li><li>Contact</li></ul></div>
        <div><h4>Legal</h4><ul><li>Terms of Use</li><li>Privacy Policy</li><li>Disclosures</li><li>Notices</li></ul></div>
      </div>
      <div class="ft-base"><span>© The Harbor Lens. All rights reserved.</span><span>Informational only. No offer, invitation or participation is implied.</span></div>
    </div>
  </footer>

</div>
</body>
</html>
```